One label design for 3 different sizes of honey bottles

Our honey company -- Amber Hollow Apiary -- needs new product labels, integrating our new name and logo. We would like one label design that presents equally well on three different sizes of plastic honey bottles. Designs should include a front and back label.

Keep in mind that we really like our old label. Please submit designs that have a similar color and font scheme as the old label.

In the uploaded files, you will find (1) detailed content instructions for each size label (2 lb, 1 lb, 8 oz), (2) photo of three plastic bottles without labels, (3) *.ai file for the new company logo, and (4) image of old package label.

Requirements
Must have
• Same look and feel as our old label, but with our new name and logo

```html
<!DOCTYPE html>
<html lang="en">
<head>
<meta charset="utf-8">
<title>Amber Hollow Apiary – Honey Labels</title>
<link href="https://fonts.googleapis.com/css2?family=Rye&family=Special+Elite&family=Courier+Prime:wght@400;700&display=swap" rel="stylesheet">
<style>
  :root{
    --paper:#ffffff;
    --cream:#fbf6e7;
    --ink:#3a3830;
    --gold:#c9a227;
    --gold-soft:rgba(201,162,39,.13);
    --sepia-soft:rgba(150,130,95,.12);
  }
  *{box-sizing:border-box;margin:0;padding:0}
  html,body{width:829px;height:1200px;overflow:hidden;background:var(--paper)}
  .sheet{position:relative;width:829px;height:1200px}

  .label{position:absolute;width:21.8em;height:29.3em;padding:.6em;
    background:var(--cream);border-radius:2.4em;
    box-shadow:0 0 0 .12em #e8dfc8;color:var(--ink);
    font-family:"Courier Prime",monospace}
  .label--small{font-size:5.8px}
  .label--medium{font-size:8.2px}
  .label--large{font-size:10px}

  .frame{position:relative;width:100%;height:100%;border:.16em solid var(--ink);
    border-radius:1.9em;box-shadow:inset 0 0 0 .35em var(--cream),inset 0 0 0 .48em var(--gold);
    display:flex;flex-direction:column;align-items:center;overflow:hidden;padding:1.4em 1em 1em}

  /* decorative placeholders */
  .art{position:absolute}
  .art--bloom{left:-.5em;top:-.5em;width:7em;height:7em;border-radius:50%;background:var(--sepia-soft)}
  .art--hive{right:.8em;bottom:4em;width:6em;height:7em;border-radius:50% 50% 1em 1em;background:var(--sepia-soft)}
  .art--map{left:50%;top:11.5em;transform:translateX(-50%);width:17em;height:8em;border-radius:.6em;background:var(--gold-soft)}
  .art--orn-left,.art--orn-right{bottom:.9em;width:4.6em;height:2.4em;border-radius:1.2em;background:rgba(58,56,48,.55)}
  .art--orn-left{left:1em}
  .art--orn-right{right:1em}

  .tagline{position:relative;font-family:"Special Elite",monospace;font-size:1.45em;letter-spacing:.02em;white-space:nowrap;line-height:1.2}
  .product{position:relative;font-family:"Rye",serif;font-weight:400;font-size:4.6em;line-height:1;letter-spacing:-.04em;
    white-space:nowrap;transform:scaleY(1.45);margin:.28em 0 .22em}
  .brand{position:relative;font-family:"Special Elite",monospace;color:var(--gold);font-size:2em;line-height:1.1;text-align:center;margin-top:.5em;white-space:nowrap}
  .net{position:relative;margin-top:auto;margin-bottom:3.4em;border:.12em solid var(--gold);border-radius:.4em;
    padding:.25em .7em;font-family:"Courier Prime",monospace;font-weight:700;font-size:1.25em;white-space:nowrap}

  /* back */
  .back .frame{padding:1.5em 1em 1em}
  .back .brand{margin-top:0;font-size:1.35em}
  .promise{position:relative;font-size:.68em;line-height:1.5;text-align:center;margin-top:.8em;white-space:nowrap}
  .rule{position:relative;width:85%;height:.08em;background:var(--ink);opacity:.5;margin:.6em 0 .5em;flex:none}
  .facts-title{position:relative;font-family:"Special Elite",monospace;font-size:1.05em;line-height:1.3;white-space:nowrap}
  .facts-title small{font-family:"Courier Prime",monospace;font-size:.65em}
  .facts{position:relative;font-size:.55em;line-height:1.45;text-align:center;white-space:nowrap}
  .note{position:relative;font-size:.48em;line-height:1.4;text-align:center;width:80%}
  .contact-row{position:relative;display:flex;align-items:center;gap:1.4em;margin-top:.9em}
  .warning{border:.1em solid var(--ink);border-radius:.3em;padding:.35em .5em;font-size:.48em;line-height:1.4;text-align:center;white-space:nowrap}
  .address{font-size:.68em;line-height:1.4;white-space:nowrap}
</style>
</head>
<body>
<main class="sheet">

  <!-- front labels -->
  <section class="label label--small front" style="left:83px;top:348px">
    <div class="frame">
      <div class="art art--bloom" role="img" aria-label="Faint line drawing of a blossom"></div>
      <div class="art art--map" role="img" aria-label="Gold outline of the home state with bee and valley scene"></div>
      <div class="art art--hive" role="img" aria-label="Faint drawing of a honey dipper"></div>
      <p class="tagline">Local • Pure • Raw</p>
      <h1 class="product">HONEY</h1>
      <p class="brand">Amber Hollow<br>Apiary</p>
      <p class="net">Net Wt. 8 oz (227 g)</p>
      <div class="art art--orn-left" role="img" aria-label="Scroll ornament"></div>
      <div class="art art--orn-right" role="img" aria-label="Scroll ornament"></div>
    </div>
  </section>

  <section class="label label--medium front" style="left:275px;top:265px">
    <div class="frame">
      <div class="art art--bloom" role="img" aria-label="Faint line drawing of a blossom"></div>
      <div class="art art--map" role="img" aria-label="Gold outline of the home state with bee and valley scene"></div>
      <div class="art art--hive" role="img" aria-label="Faint drawing of a honey dipper"></div>
      <p class="tagline">Local • Pure • Raw</p>
      <h1 class="product">HONEY</h1>
      <p class="brand">Amber Hollow<br>Apiary</p>
      <p class="net">Net Wt. 1 LB (454 g)</p>
      <div class="art art--orn-left" role="img" aria-label="Scroll ornament"></div>
      <div class="art art--orn-right" role="img" aria-label="Scroll ornament"></div>
    </div>
  </section>

  <section class="label label--large front" style="left:529px;top:195px">
    <div class="frame">
      <div class="art art--bloom" role="img" aria-label="Faint line drawing of a blossom"></div>
      <div class="art art--map" role="img" aria-label="Gold outline of the home state with bee and valley scene"></div>
      <div class="art art--hive" role="img" aria-label="Faint drawing of a honey dipper"></div>
      <p class="tagline">Local • Pure • Raw</p>
      <h1 class="product">HONEY</h1>
      <p class="brand">Amber Hollow<br>Apiary</p>
      <p class="net">Net Wt. 2 LB (907 g)</p>
      <div class="art art--orn-left" role="img" aria-label="Scroll ornament"></div>
      <div class="art art--orn-right" role="img" aria-label="Scroll ornament"></div>
    </div>
  </section>

  <!-- back labels -->
  <section class="label label--small back" style="left:83px;top:965px">
    <div class="frame">
      <div class="art art--bloom" role="img" aria-label="Faint line drawing of a blossom"></div>
      <div class="art art--hive" role="img" aria-label="Faint drawing of a honey dipper"></div>
      <p class="brand">Amber Hollow Apiary</p>
      <p class="promise">Amber Hollow Apiary promises 100% pure honey,<br>never pasteurized,<br>and sourced exclusively from beehives we keep<br>near Millbrook Falls, West Virginia</p>
      <div class="rule"></div>
      <p class="facts-title">Nutrition Facts <small>Servings: 11,</small></p>
      <p class="facts">Serv. size: 1 Tbsp (21g),<br>Amount per serving: Calories 60,<br>Total Fat 0g (0% DV), Sat. Fat 0g (0% DV), Trans Fat 0g,<br>Cholest. 0mg (0% DV), Sodium 0mg (0% DV),<br>Total Carb. 17g (6% DV), Fiber 0g (0% DV),<br>Total Sugars 17g (34% DV*), Protein 0g, Vit. D (0% DV),<br>Calcium (0% DV), Iron (0% DV), Potas. (0% DV).</p>
      <div class="rule"></div>
      <p class="note">*One serving adds 17g of sugar to your diet and represents 34% of the Daily Value for Added Sugars.</p>
      <div class="contact-row">
        <p class="warning">DO NOT FEED HONEY<br>TO INFANTS<br>UNDER ONE YEAR</p>
        <p class="address">Amber Hollow Apiary<br>18 Linden Ridge Road<br>Millbrook Falls, WV 25000<br>www.amberhollowapiary.com</p>
      </div>
      <div class="art art--orn-left" role="img" aria-label="Scroll ornament"></div>
      <div class="art art--orn-right" role="img" aria-label="Scroll ornament"></div>
    </div>
  </section>

  <section class="label label--medium back" style="left:275px;top:879px">
    <div class="frame">
      <div class="art art--bloom" role="img" aria-label="Faint line drawing of a blossom"></div>
      <div class="art art--hive" role="img" aria-label="Faint drawing of a honey dipper"></div>
      <p class="brand">Amber Hollow Apiary</p>
      <p class="promise">Amber Hollow Apiary promises 100% pure honey,<br>never pasteurized,<br>and sourced exclusively from beehives we keep<br>near Millbrook Falls, West Virginia</p>
      <div class="rule"></div>
      <p class="facts-title">Nutrition Facts <small>Servings: 22,</small></p>
      <p class="facts">Serv. size: 1 Tbsp (21g),<br>Amount per serving: Calories 60,<br>Total Fat 0g (0% DV), Sat. Fat 0g (0% DV), Trans Fat 0g,<br>Cholest. 0mg (0% DV), Sodium 0mg (0% DV),<br>Total Carb. 17g (6% DV), Fiber 0g (0% DV),<br>Total Sugars 17g (34% DV*), Protein 0g, Vit. D (0% DV),<br>Calcium (0% DV), Iron (0% DV), Potas. (0% DV).</p>
      <div class="rule"></div>
      <p class="note">*One serving adds 17g of sugar to your diet and represents 34% of the Daily Value for Added Sugars.</p>
      <div class="contact-row">
        <p class="warning">DO NOT FEED HONEY<br>TO INFANTS<br>UNDER ONE YEAR</p>
        <p class="address">Amber Hollow Apiary<br>18 Linden Ridge Road<br>Millbrook Falls, WV 25000<br>www.amberhollowapiary.com</p>
      </div>
      <div class="art art--orn-left" role="img" aria-label="Scroll ornament"></div>
      <div class="art art--orn-right" role="img" aria-label="Scroll ornament"></div>
    </div>
  </section>

  <section class="label label--large back" style="left:529px;top:808px">
    <div class="frame">
      <div class="art art--bloom" role="img" aria-label="Faint line drawing of a blossom"></div>
      <div class="art art--hive" role="img" aria-label="Faint drawing of a honey dipper"></div>
      <p class="brand">Amber Hollow Apiary</p>
      <p class="promise">Amber Hollow Apiary promises 100% pure honey,<br>never pasteurized,<br>and sourced exclusively from beehives we keep<br>near Millbrook Falls, West Virginia</p>
      <div class="rule"></div>
      <p class="facts-title">Nutrition Facts <small>Servings: 22,</small></p>
      <p class="facts">Serv. size: 1 Tbsp (21g),<br>Amount per serving: Calories 60,<br>Total Fat 0g (0% DV), Sat. Fat 0g (0% DV), Trans Fat 0g,<br>Cholest. 0mg (0% DV), Sodium 0mg (0% DV),<br>Total Carb. 17g (6% DV), Fiber 0g (0% DV),<br>Total Sugars 17g (34% DV*), Protein 0g, Vit. D (0% DV),<br>Calcium (0% DV), Iron (0% DV), Potas. (0% DV).</p>
      <div class="rule"></div>
      <p class="note">*One serving adds 17g of sugar to your diet and represents 34% of the Daily Value for Added Sugars.</p>
      <div class="contact-row">
        <p class="warning">DO NOT FEED HONEY<br>TO INFANTS<br>UNDER ONE YEAR</p>
        <p class="address">Amber Hollow Apiary<br>18 Linden Ridge Road<br>Millbrook Falls, WV 25000<br>www.amberhollowapiary.com</p>
      </div>
      <div class="art art--orn-left" role="img" aria-label="Scroll ornament"></div>
      <div class="art art--orn-right" role="img" aria-label="Scroll ornament"></div>
    </div>
  </section>

</main>
</body>
</html>
```